Major Australian Food and Wine Event Web Design Project

The project will consist of 3 designs
The homepage
A city hub page
A general content page

The main audience who will visit the website will be (in Order of importance:

1) Visitors
- Mainly women 24 – 54 years (they are the main ticket buyers)
- In a relationship – so will go to the show with their partner
- In a good paying job or home maker – and who have disposable income to spend $30 a ticker
- Enjoy food, wine and going out
- Looking for a fun day out – although an event that is about food and wine – it is an event that most people will go to and have a fun day out – not too pretentious

A smaller proportion of the audience will be:
2) Exhibitors & sponsors ( both prospective and existing)
3) Media

Objectives:

- Functionality on home page and sub pages needs to be updated, clear, easy to navigate and inject a sense of ‘fun’ – need to make it look more professional
- Need to incorporate the many things that need to be on the home page and sub pages in a visually appealing manner
- Ensure the ‘Cons’ above are considered and reflected in functionality and design
- To not be too focus on the colours (these can be changed) – but focus on the functionality and overall design opportunities.

Approach:

Keywords to describe the Bright Plate & Vine Fair:
Fun day out, discover, learn, indulge, entertaining

Other website examples:

Some great consumers event websites from the UK really make our website look basic and juvenile – and below are some examples of the presentation of how we would like our website to look like:

http://www.morselfairs-example.com/london/ This website is clean, includes good social media integration and exudes a sense of fun. Their content pages, such as the features landing page also presents options in a clear and visually appealing way with a series of boxes including image and text http://www.morselfairs-example.com/london/content/343/Features

http://www.homecraftexpo-example.com/ - this is also a great website – and it incorporates all the elements we would be looking for on our homepage – but the background/skin also includes a sense of fun and cheekiness. Subpages also are consistent.

Features

• Its a fun day that offers great value for money
• Caters to all visitors, regardless of different levels of knowledge or interest in food, wine and cooking.
• Sample great quality food and wine products from hundreds of reputable exhibitors
• Learn more through many of the shows feature activities (Celeb Theatre, Wine Theatre, Cooking & Cheese Classes)

Functionality & Structure:

In a user friendly, easy to view way, we need to incorporate the following functionality elements on home page:
- main header (that will incorporate our current creative) with a ‘fun’ skin
- navigation tabs/references (hone, location, tickets, blog, sign up, exhibitors)
- navigation/content banner (rotating)
- Area for small intro about the show
- News and highlight section
- New exhibitors section
- Obvious Ticket call to action
- Obvious sign up call to action
- Social media buttons or links ( really like the moving gifs on the Homecraftexpo-example.com site
- area for advertising (MREC size) to sell to exhibitors/sponsors
- Show dates for all 5 shows (maybe in main header)

Subpage layout is also important and needs to reflect the homepage – so would also like to see examples of how this would look and tie in with navigation – we generally have a lot of content on these pages, so clear navigation would be useful. – see below for further details of functionality for city Hubs

‘CITY HUB’ BRIEF
When navigating to each location the user will be taken to a ‘CITY HUB’ which should replicate design and content elements of a main HOME page, as well as reflect more specific information for each Show. Elements which must appear on this page are:
• FEATURES – which may be displayed in categories (in boxes, see appendix 1.0) which will link through to relevant content pages. Or in one box which will link through to a features page with all presented in boxes
• CHEFS – may be displayed as a separate icon box which will link to chefs page with bios, Celeb Theatre timetable etc.
• TICKETS – either a button or clear callout to purchase tickets
• PLAN YOUR DAY – may be displayed in a separate content box which will then link through to getting there, sample itineraries and downloadable pocket show guide for visitors to print before coming to the Show.
• WHO’S EXHIBITING – to link back to city specific exhibitor lists

Our current website is out of date and has the following inadequacies (www.brightplatefair-example.com.au) -

The homepage
A city hub page
A general content page

1) Visitors

3) Media

Objectives:

Approach:

To be perceived as a fun, entertaining event with something for everyone - website creative and navigation must reflect this.

Other website examples:

Features

- New exhibitors section

‘CITY HUB’ BRIEF

- Dated design/layout
- Homepage too text heavy
- No content boxes that can be used for different features/areas (eg. News, Exhibitors etc)
- Uninspiring colours and skin(eg. grey background), does not reflect ‘a fun day out’
- Limited presence of social media platforms and lacks ‘community’
- No continuity in sub pages
- main banner too big – takes up too much space on homepage

Requirements
Must have
• As per above brief.

In addition:
Floating social media buttons on side
Wrap around image
Drop down menu (specifically for the location nav item)

```html
<!DOCTYPE html>
<html lang="en">
<head>
<meta charset="utf-8">
<title>Bright Plate &amp; Vine Fair</title>
<link href="https://fonts.googleapis.com/css2?family=Questrial&family=Arimo:wght@400;700&family=Oswald:wght@500&display=swap" rel="stylesheet">
<style>
:root{
  --sky-top:#7cc6f3;
  --sky-bottom:#bfe4fb;
  --panel:#ffffff;
  --panel-edge:#d9eefa;
  --blue:#2aaef0;
  --blue-dark:#138fd3;
  --blue-light:#8fd3f7;
  --tab-dark:#1e1e1e;
  --red:#b5121b;
  --red-dark:#8d0c12;
  --text:#222222;
  --muted:#666666;
  --rule:#cfcfcf;
  --grey-box:#f3f3f3;
}
*{box-sizing:border-box;margin:0;padding:0}
html,body{width:1200px;height:921px;overflow:hidden}
body{
  position:relative;
  background:linear-gradient(180deg,var(--sky-top) 0%,var(--sky-bottom) 55%,var(--sky-top) 100%);
  font-family:"Arimo",Arial,sans-serif;color:var(--text);
}
.abs{position:absolute}
.brand{left:121px;top:12px;width:160px;height:125px;background:#fff;border:4px solid #2b2b2b;border-radius:12px;
  box-shadow:0 3px 6px rgba(0,0,0,.35);display:flex;align-items:center;justify-content:center;text-align:center;
  font-family:"Questrial",sans-serif;font-size:21px;line-height:1.15;color:#222;padding:8px}
.top-links{right:122px;top:9px;font-family:"Questrial",sans-serif;font-size:13px;color:#111}
.top-links span{margin:0 6px}
.top-links i{color:#9ab;font-style:normal}
.plates{left:462px;top:48px}
.panel{left:105px;top:150px;width:990px;height:790px;background:var(--panel);border:5px solid var(--panel-edge);border-radius:12px}
.nav{left:120px;top:167px;display:flex}
.nav a{display:block;height:35px;width:100px;margin-right:-3px;background:var(--tab-dark);color:#fff;text-decoration:none;
  font-family:"Questrial",sans-serif;font-size:13px;line-height:35px;text-align:center;border-radius:18px;border:1px solid #555;box-shadow:0 3px 4px rgba(0,0,0,.25)}
.nav a.current{background:linear-gradient(#5cc8f7,var(--blue-dark));width:104px;position:relative;z-index:2}
.search{left:780px;top:167px;width:300px;height:34px;border:1px solid #b8dff5;border-radius:17px;background:linear-gradient(#fff,#eef4f7);
  font-family:"Questrial",sans-serif;font-size:14px;color:#888;padding:9px 16px}
.search-btn{left:1046px;top:169px;width:32px;height:30px;border-radius:50%;background:var(--blue)}
.banner{left:120px;top:227px;width:640px;height:290px;border-radius:10px;overflow:hidden;border:1px solid #999;
  background:linear-gradient(180deg,#d8dcd8 0%,#9a9a98 45%,#5a5a58 100%)}
.caption{position:absolute;left:0;bottom:0;width:100%;height:70px;background:rgba(40,40,40,.72);padding:7px 14px;color:#fff}
.caption h3{font-family:"Questrial",sans-serif;font-weight:400;font-size:19px}
.caption p{font-size:12px;line-height:13px;margin-top:4px}
.dots{left:418px;top:521px;display:flex;gap:5px}
.dots b{width:10px;height:10px;border-radius:50%;background:#666}
.dots b:first-child{background:var(--red)}
.welcome{left:120px;top:564px;font-family:"Questrial",sans-serif;font-weight:400;font-size:24px;color:#111}
.welcome em{font-style:normal;color:var(--red)}
.intro{left:120px;top:612px;width:642px;font-size:12px;line-height:18px}
.intro p{margin-bottom:17px}
.tabs{display:flex;gap:4px;border-bottom:3px solid var(--blue)}
.tabs span{font-family:"Questrial",sans-serif;font-size:16px;color:#fff;background:var(--blue);padding:4px 13px 3px;border-radius:8px 8px 0 0}
.tabs span.off{background:var(--blue-light)}
.box{border:1px solid #ddd;border-top:none;height:90px;padding:20px 10px}
.news{left:120px;top:820px;width:310px}
.exhib{left:450px;top:820px;width:310px}
.thumb{float:left;width:92px;height:60px;background:linear-gradient(#d6d6d6,#8f8f8f);margin-right:10px;border:1px solid #aaa}
.item h4{font-family:"Questrial",sans-serif;font-weight:400;color:var(--red);font-size:14px}
.exhib .item h4{font-size:17px}
.item p{font-size:12px;line-height:16px;margin-top:4px;color:#333}
.item small{color:var(--muted);font-size:11px}
.ticket-cta{left:780px;top:227px;width:300px;height:88px;border-radius:10px;background:linear-gradient(#e23a34,var(--red) 60%,var(--red-dark));
  border:2px solid var(--red-dark);box-shadow:0 4px 6px rgba(0,0,0,.3);color:#fff;padding:16px 14px}
.ticket-cta strong{display:block;font-family:"Oswald",sans-serif;font-weight:500;font-size:26px;line-height:30px}
.ticket-cta span{font-family:"Questrial",sans-serif;font-size:17px}
.shows{left:780px;top:343px;width:300px;height:312px;border:1px solid #ccc;border-radius:10px;background:linear-gradient(#fff 60%,var(--grey-box));padding:8px 11px}
.shows h2{font-family:"Questrial",sans-serif;font-weight:400;font-size:18px;color:var(--blue);border-bottom:3px solid var(--blue);padding-bottom:2px}
.show{display:flex;align-items:center;height:52.4px;border-bottom:1px dashed var(--rule)}
.show i{width:44px;height:34px;border:1px solid #bbb;background:#fafafa;margin-right:16px}
.show b{display:block;font-weight:400;color:var(--red);font-size:14px}
.show small{color:var(--muted);font-size:12px}
.video{left:780px;top:683px;width:300px;height:231px;border:1px solid #ccc;border-radius:10px;background:#2c2c2c;overflow:hidden}
.video-frame{position:absolute;left:7px;top:7px;width:284px;height:183px;background:linear-gradient(#cfd7dd,#7f8a92 60%,#3c4248)}
.video-label{position:absolute;left:10px;bottom:10px;color:#fff;font-size:12px}
.social{left:1090px;top:205px;width:57px;height:145px;background:#fff;border:4px solid var(--panel-edge);border-left:none;border-radius:0 10px 10px 0;padding:10px 8px}
.social i{display:block;width:32px;height:32px;border-radius:5px;background:#c9d5e2;margin-bottom:11px}
</style>
</head>
<body>
<div class="abs brand">Bright Plate &amp; Vine Fair</div>
<div class="abs top-links"><span>Login</span><i>|</i><span>Sign Up</span><i>|</i><span>Contact</span></div>

<svg class="abs plates" width="620" height="110" viewBox="0 0 620 110">
  <path d="M0 110 Q0 20 82 18 Q125 18 150 40 Q180 10 220 12 Q260 12 290 40 Q320 12 360 12 Q400 12 430 40 Q460 12 500 12 Q560 14 615 60 L615 110Z" fill="#e4e4e4"/>
  <circle cx="86" cy="72" r="62" fill="#e23a1c" role="img" aria-label="Fresh tomato"/>
  <circle cx="222" cy="80" r="60" fill="#2a4a1e" role="img" aria-label="Pan of prawns and greens"/>
  <circle cx="362" cy="80" r="60" fill="#e8d8b8" role="img" aria-label="Sushi roll"/>
  <circle cx="502" cy="80" r="60" fill="#3c5a4c" role="img" aria-label="Ship's wheel decoration"/>
</svg>

<div class="abs panel"></div>

<nav class="abs nav">
  <a class="current">HOME</a><a>LOCATION</a><a>TICKETS</a><a>BLOG</a><a>SIGN UP</a><a>EXHIBITORS</a>
</nav>
<div class="abs search">Search</div>
<svg class="abs search-btn" viewBox="0 0 32 30"><circle cx="14" cy="13" r="6" fill="none" stroke="#fff" stroke-width="3"/><path d="M18 17 L24 23" stroke="#fff" stroke-width="3"/></svg>

<div class="abs banner" role="img" aria-label="Group of celebrity chefs at the fair">
  <div class="caption">
    <h3>EXIBITORS NAME</h3>
    <p>It is a long established fact that a reader will be distracted by the readable content of a page when looking at its layout.</p>
  </div>
</div>
<div class="abs dots"><b></b><b></b><b></b></div>

<h1 class="abs welcome">Welcome to <em>The Bright Plate &amp; Vine Fair</em></h1>
<div class="abs intro">
  <p>What a year for good food and wine!</p>
  <p>Melbourne, Sydney, Perth, Adelaide and Brisbane have all had the chance to experience the fun, excitement and joy, that is the Bright Plate &amp; Vine Fair!</p>
  <p>We would like to thank all our amazing visitors for coming along and helping us celebrate another awesome year - A big thank you also to the rest of the crew including exhibitors, sponsors and chefs!</p>
  <p>Make sure you visit the website early next year for all the details of the 2012 Shows - or sign up to our newsletter to be the first to find out when we are on sale and to receive special discounts and offers!</p>
</div>

<section class="abs news">
  <div class="tabs"><span>NEWS</span><span class="off">HIGHTLIGHT</span></div>
  <div class="box item"><div class="thumb" role="img" aria-label="Chefs in a kitchen"></div>
    <h4>Harbour &amp; Lane Celebrity</h4><p><small>21 Feb 2012</small> Despite a drizzly start to the UK's...</p></div>
</section>
<section class="abs exhib">
  <div class="tabs"><span>EXIBITORS</span></div>
  <div class="box item"><div class="thumb" role="img" aria-label="Exhibitor stand"></div>
    <h4>Harbour &amp; Lane Celebrity</h4></div>
</section>

<a class="abs ticket-cta"><strong>TICKETS AVAILABLE NOW!</strong><span>Click here or call 613 5550 1827</span></a>

<aside class="abs shows">
  <h2>UPCOMING SHOW</h2>
  <div class="show"><i></i><div><b>Melbourne</b><small>01 June 2012 to 03 June 2012</small></div></div>
  <div class="show"><i></i><div><b>Sydney</b><small>22 June 2012 to 24 June 2012</small></div></div>
  <div class="show"><i></i><div><b>Perth</b><small>13 July 2012 to 15 July 2012</small></div></div>
  <div class="show"><i></i><div><b>Adelaida</b><small>12 Oct 2012 to 14 Oct 2012</small></div></div>
  <div class="show"><i></i><div><b>Brisbane</b><small>09 Nov 2012 to 11 Nov 2012</small></div></div>
</aside>

<div class="abs video">
  <div class="video-frame" role="img" aria-label="Video still of the fair information point"></div>
  <svg class="abs" style="left:22px;top:156px" width="255" height="26" viewBox="0 0 255 26">
    <rect x="0" y="0" width="26" height="26" rx="3" fill="#111"/><path d="M9 6 L19 13 L9 20Z" fill="#fff"/>
    <rect x="35" y="0" width="172" height="26" rx="3" fill="#111"/><rect x="43" y="11" width="60" height="4" fill="#fff"/>
    <text x="114" y="17" fill="#fff" font-size="10" font-family="Arimo,sans-serif">00:00</text>
    <rect x="152" y="9" width="46" height="8" fill="#3aa6e0"/>
    <rect x="216" y="0" width="26" height="26" rx="3" fill="#111"/><path d="M221 5h5M221 5v5M237 21h-5M237 21v-5" stroke="#fff" stroke-width="2"/>
  </svg>
  <svg class="abs" style="left:136px;top:70px" width="40" height="40"><circle cx="20" cy="20" r="19" fill="rgba(0,0,0,.6)"/><path d="M15 11 L28 20 L15 29Z" fill="#fff"/></svg>
  <span class="video-label">Bright Plate &amp; Vine Fair</span>
</div>

<div class="abs social"><i></i><i></i><i></i></div>
</body>
</html>
```